Webdesign für Waldhain Imkerei
Zielgruppe
Imkerei, Verkauf von Honig und Honigerzeugnissen, so wie Bienenwachskerzen.
Zielgruppe sind vermutlich Frauen im mittleren bis gehobenen Alter.
Aufgabenstellung
Es gibt ein Firmenlogo.
Ich bevorzuge als Grundfarbe weiß, lasse mich aber von guten Einfällen gerne überraschen.
Die Website www.velmique.at finde ich sehr ansprechend.
Nur ohne Musik.
Ohne Deutsch/Englisch Auswahl.
Es soll danach Word press verwendet werden.

```html
<!DOCTYPE html>
<html lang="de">
<head>
<meta charset="utf-8">
<title>Waldhain Imkerei – Honig mit Orange</title>
<link href="https://fonts.googleapis.com/css2?family=Roboto:wght@400;500;700&family=Roboto+Condensed:wght@400;700&family=Lato:wght@300;400&display=swap" rel="stylesheet">
<style>
:root{
  --bg:#efefef;
  --page:#ffffff;
  --ink:#222222;
  --muted:#777777;
  --line:#e3e3e3;
  --honey:#f7a731;
  --brown:#4a2a12;
  --link:#4a8fcc;
}
*{margin:0;padding:0;box-sizing:border-box}
html,body{width:843px;height:1200px;overflow:hidden;background:var(--bg)}
body{font-family:"Roboto",Arial,sans-serif;color:var(--ink)}
.stage{position:absolute;left:0;top:0;width:1591px;height:2265px;transform:scale(.5299);transform-origin:0 0}
.page{position:absolute;left:75px;top:75px;width:1441px;height:2108px;background:var(--page)}
.abs{position:absolute}
.topbar{left:0;top:0;width:1441px;height:34px;border-bottom:1px solid var(--line)}
.topbar .item{position:absolute;top:0;height:34px;line-height:34px;font-size:9px;letter-spacing:1px;font-weight:500;text-align:center;border-left:1px solid var(--line)}
.brand{left:570px;top:118px;width:300px;text-align:center;font-family:"Roboto Condensed",sans-serif;font-weight:700;font-size:17px;letter-spacing:1px;color:var(--brown)}
.brand-mark{left:700px;top:45px;width:40px;height:40px;border:4px solid var(--brown)}
.nav{top:121px;font-family:"Roboto Condensed",sans-serif;font-size:11px;letter-spacing:1.6px;color:#555}
.nav.active{color:var(--honey)}
.header-rule{left:0;top:155px;width:1441px;border-top:1px solid var(--line)}
.crumb{left:265px;top:169px;font-size:9px;letter-spacing:.8px;color:var(--muted)}
.crumb b{color:var(--ink);font-weight:500}
.thumb{left:290px;width:61px;height:61px}
.photo{left:410px;top:212px;width:339px;height:340px;background:radial-gradient(circle at 50% 50%,#d9a23c 0 22%,#ececec 40%,#e4e4e4 100%)}
.arrow{font-size:26px;color:#777;font-weight:300}
.stars{left:823px;top:210px;font-size:11px;color:#aaa;letter-spacing:1px}
.stars a{color:var(--link);font-size:10px;letter-spacing:0;margin-left:6px;text-decoration:none}
.ptitle{left:823px;top:234px;font-size:14px;color:#444}
.pdesc{left:823px;top:270px;width:254px;font-size:9.5px;line-height:16.7px;text-align:justify}
.label{font-size:9.5px;font-weight:500;letter-spacing:.3px}
.field{left:825px;width:251px;height:30px;border:1px solid #ccc}
.price{left:826px;top:460px;font-size:13px;color:var(--honey)}
.price small{font-size:9px;color:var(--ink);font-style:italic}
.price small a{color:var(--link);text-decoration:none}
.facts{left:827px;top:491px;font-size:9.5px;line-height:17px}
.facts b{font-weight:700}
.cart{left:828px;top:553px;width:248px;height:31px;background:var(--honey);color:#fff;font-size:10px;letter-spacing:1.3px;line-height:31px;text-align:center;font-weight:500}
.tabs{left:365px;top:622px;width:695px;height:33px;border-top:1px solid var(--line)}
.tab{position:absolute;top:8px;font-size:10px;color:#999}
.tab.on{color:var(--ink)}
.tabbar{left:365px;top:652px;width:695px;height:3px;background:#ddd}
.tabbar i{position:absolute;left:0;top:0;width:232px;height:3px;background:#555}
.opts{left:365px;top:679px;width:695px;text-align:center;font-size:9.5px;color:var(--link);word-spacing:1px}
.opts span{margin:0 6px}
.acc{left:365px;width:692px;height:20px;border-bottom:1px solid #ccc;font-size:10.5px;font-weight:500;letter-spacing:.3px}
.acc svg{position:absolute;right:4px;top:3px}
.h-small{left:365px;top:783px;font-size:11.5px;letter-spacing:.4px}
.copy{left:365px;width:692px;font-size:9.5px;line-height:18px;text-align:justify}
.copy.bold{font-weight:700}
.band{left:275px;top:1075px;width:901px;height:224px;background:linear-gradient(100deg,#e2e2e2,#f3f3f3 45%,#e6e6e6 70%,#dcdcdc)}
.band h2{position:absolute;left:0;top:68px;width:901px;text-align:center;font-family:"Lato",sans-serif;font-weight:300;font-size:22px;letter-spacing:1.6px;color:#333}
.band .input{position:absolute;left:245px;top:114px;width:256px;height:32px;background:#fff;border:1px solid #d6d6d6;font-size:9.5px;color:#888;line-height:30px;padding-left:14px}
.band .send{position:absolute;left:506px;top:114px;width:135px;height:32px;background:var(--honey);color:#fff;font-size:9.5px;letter-spacing:1.5px;line-height:32px;text-align:center;font-weight:500}
.h-lead{left:0;top:1350px;width:1441px;text-align:center;font-family:"Lato",sans-serif;font-weight:300;font-size:22px;letter-spacing:2.4px;color:#333}
.story{left:350px;width:745px;font-size:9.5px;line-height:16.6px;color:#777;text-align:justify}
.story b{color:var(--ink);font-weight:500}
.footer-rule{left:265px;top:1701px;width:900px;height:2px;background:var(--honey)}
.fcol{top:1734px;width:210px;font-size:9.5px;line-height:18px;color:#777}
.fcol h4{font-size:10.5px;color:var(--ink);font-weight:700;margin-bottom:18px}
.fcol b{color:var(--ink);font-weight:400}
.social{left:277px;top:1935px}
.social i{display:inline-block;width:9px;height:9px;border-radius:50%;background:#555;margin-right:16px}
.bottom-rule{left:0;top:1987px;width:1441px;border-top:1px solid var(--line)}
.legal{left:0;top:2018px;width:1441px;text-align:center;font-size:9.5px;color:#777}
.pay{top:2042px;width:41px;height:26px;border:1px solid #ddd;background:#f6f6f6}
</style>
</head>
<body>
<div class="stage">
<div class="page">

  <div class="abs topbar">
    <div class="item" style="left:916px;width:98px">MEIN KONTO ⌄</div>
    <div class="item" style="left:1013px;width:151px;border-right:1px solid var(--line)">&#9632; WARENKORB</div>
  </div>

  <div class="abs brand-mark" aria-hidden="true"></div>
  <div class="abs brand">WALDHAIN IMKEREI</div>

  <div class="abs nav" style="left:310px">STARTSEITE</div>
  <div class="abs nav" style="left:417px">DIE MANUFAKTUR</div>
  <div class="abs nav" style="left:553px">DER HONIG</div>
  <div class="abs nav" style="left:821px">DAS BIENENWACHS</div>
  <div class="abs nav active" style="left:975px">DER SHOP</div>
  <div class="abs nav" style="left:1083px">KONTAKT</div>
  <div class="abs header-rule"></div>

  <div class="abs crumb">HOME &nbsp;/&nbsp; SHOP &nbsp;/&nbsp; HONIGPRODUKTE &nbsp;/&nbsp; <b>HONIG MIT ORANGE</b></div>

  <div class="abs thumb" style="top:234px;background:linear-gradient(#f3f3f3,#e3b04f 60%,#eee)" role="img" aria-label="Honigglas"></div>
  <div class="abs thumb" style="top:310px;background:linear-gradient(#9a8cc0,#5d8a3c)" role="img" aria-label="Blumenwiese"></div>
  <div class="abs thumb" style="top:384px;background:linear-gradient(135deg,#8b7b8f,#e6a63a)" role="img" aria-label="Honig mit Lavendel"></div>
  <div class="abs thumb" style="top:459px;background:linear-gradient(135deg,#f2e6d6,#d9913a)" role="img" aria-label="Brot mit Honig"></div>

  <div class="abs photo" role="img" aria-label="Produktfoto Honigglas mit Etikett"></div>
  <div class="abs arrow" style="left:379px;top:360px">‹</div>
  <div class="abs arrow" style="left:766px;top:360px">›</div>

  <div class="abs stars">★★★★★<a>8 Bewertungen lesen</a></div>
  <div class="abs ptitle">Honig mit Orange, Honigspezialität</div>
  <div class="abs pdesc">Lorem ipsum dolor sit amet, consetetur sadipscing elitr, sed diam nonumy eirmod tempor invidunt ut labore et dolore magna aliquyam erat, sed diam voluptua.</div>

  <div class="abs label" style="left:825px;top:336px">HONIG MIT ORANGE</div>
  <div class="abs field" style="top:353px">
    <svg style="position:absolute;right:8px;top:11px" width="9" height="6"><path d="M1 1 L4.5 4.5 L8 1" fill="none" stroke="#222" stroke-width="1.4"/></svg>
  </div>
  <div class="abs label" style="left:825px;top:395px">HONIG MIT ORANGE</div>
  <div class="abs field" style="top:412px;font-size:11px;line-height:28px">
    <span style="position:absolute;left:10px">–</span><span style="position:absolute;left:123px">1</span><span style="position:absolute;right:10px">+</span>
  </div>
  <div class="abs price">€5,95 <small>Inkl. Mwst.; zzgl. <a>Versandkosten</a></small></div>
  <div class="abs facts"><b>Verfügbarkeit:</b> Auf Lager<br><b>Lieferzeit:</b> 3-5 Tage<br><b>Grundpreis:</b> €6,95 / 100 g</div>
  <div class="abs cart">IN DEN WARENKORB</div>

  <div class="abs tabs">
    <div class="tab on" style="left:14px">OPTIONEN</div>
    <div class="tab" style="left:248px">TEILEN</div>
    <div class="tab" style="left:478px">SCHLAGWORTE</div>
  </div>
  <div class="abs tabbar"><i></i></div>

  <div class="abs opts"><span>✉ Anfrage zu diesem Produkt</span><span>♥ Auf den Wunschzettel</span><span>◫ + Auf Vergleichsliste setzen</span><span>⎙ Drucken</span></div>

  <div class="abs acc" style="top:737px">BESCHREIBUNG<svg width="9" height="6"><path d="M1 5 L4.5 1.5 L8 5" fill="none" stroke="#222" stroke-width="1.4"/></svg></div>
  <div class="abs h-small">GESCHMACK</div>
  <div class="abs copy bold" style="top:819px">Lorem ipsum dolor sit amet, consetetur sadipscing elitr, sed diam nonumy eirmod tempor invidunt ut labore et dolore magna aliquyam erat, sed diam voluptua. At vero eos et accusam et justo duo dolores et ea rebum. Stet clita kasd gubergren, no sea takimata sanctus est Lorem ipsum dolor sit amet accusam et justo duo dolores et ea rebum. Stet clita kasd.</div>
  <div class="abs copy" style="top:891px">Lorem ipsum dolor sit amet, consetetur sadipscing elitr, sed diam nonumy eirmod tempor invidunt ut labore et dolore magna aliquyam erat, sed diam voluptua. At vero eos et accusam et justo duo dolores et ea rebum. Stet clita kasd gubergren, no sea takimata sanctus est Lorem ipsum dolor sit amet. Lorem ipsum dolor sit amet, consetetur sadipscing elitr.</div>
  <div class="abs acc" style="top:974px">BEWERTUNGEN (20)<svg width="9" height="6"><path d="M1 1 L4.5 4.5 L8 1" fill="none" stroke="#222" stroke-width="1.4"/></svg></div>

  <div class="abs band" role="img" aria-label="Hintergrundfoto mit Bienen, hell und unscharf">
    <h2>JETZT FÜR UNSEREN AKTUELLEN NEWSLETTER ANMELDEN</h2>
    <div class="input">E-Mail Adresse hier eingeben ...</div>
    <div class="send">ABSENDEN</div>
  </div>

  <div class="abs h-lead">EXKLUSIVER HONIG AUS DEM PFÄLZERWALD</div>
  <div class="abs story" style="top:1418px"><b>Lorem ipsum dolor sit amet, consetetur sadipscing elitr, sed diam nonumy eirmod tempor invidunt</b><br>Lorem ipsum dolor sit amet, consetetur sadipscing elitr, sed diam nonumy eirmod tempor invidunt ut labore et dolore magna aliquyam erat, sed diam voluptua. At vero eos et accusam et justo duo dolores et ea rebum. Stet clita kasd gubergren, no sea takimata sanctus est Lorem ipsum dolor sit amet. Lorem ipsum dolor sit amet, consetetur sadipscing elitr, sed diam nonumy eirmod tempor invidunt ut labore et dolore magna aliquyam erat, sed diam voluptua. At vero eos et accusam et justo duo dolores et ea rebum. Stet clita kasd gubergren, no sea takimata sanctus est Lorem ipsum dolor sit amet. Lorem ipsum dolor sit amet, consetetur sadipscing elitr, sed diam nonumy eirmod tempor invidunt ut labore.</div>
  <div class="abs story" style="top:1534px"><b>Lorem ipsum dolor sit amet, consetetur sadipscing elitr, sed diam nonumy eirmod tempor invidunt</b><br>Lorem ipsum dolor sit amet, consetetur sadipscing elitr, sed diam nonumy eirmod tempor invidunt ut labore et dolore magna aliquyam erat, sed diam voluptua. At vero eos et accusam et justo duo dolores et ea rebum. Stet clita kasd gubergren, no sea takimata sanctus est Lorem ipsum dolor sit amet. Lorem ipsum dolor sit amet, consetetur sadipscing elitr, sed diam nonumy eirmod tempor invidunt ut labore et dolore magna aliquyam erat, sed diam voluptua. At vero eos et accusam et justo duo dolores et ea rebum. Stet clita kasd gubergren, no sea takimata sanctus est Lorem ipsum dolor sit amet. Lorem ipsum dolor sit amet, consetetur sadipscing elitr, sed diam nonumy eirmod tempor invidunt ut labore et</div>

  <div class="abs footer-rule"></div>
  <div class="abs fcol" style="left:275px"><h4>Waldhain Imkerei © 2018</h4>Lorem ipsum dolor sit amet, consetetur sadipscing elitr, sed diam nonumy eirmod tempor invidunt ut labore et dolore magna aliquyam erat, sed diam voluptua. Lorem ipsum dolor sit amet, consetetur sadipscing<br><br><b>Telefon:</b> 0000 000 0000<br><b>E-Mail:</b> service@waldhain-imkerei.de</div>
  <div class="abs fcol" style="left:500px"><h4>Unternehmen</h4>Die Manufaktur<br>Der Honig<br>Das Bienenwachs<br>Kontaktformular<br>Datenschutz<br>Impressum</div>
  <div class="abs fcol" style="left:725px"><h4>Service</h4>FAQ<br>Lieferung &amp; Versand<br>AGB<br>Widerrufsbelehrung<br>Widerrufsformular<br>Glossar<br>Kundenmeinungen</div>
  <div class="abs fcol" style="left:950px"><h4>Mein Konto</h4>Kundenkonto anlegen<br>Meine Bestellungen<br>Meine Nachrichten<br>Mein Wunschzettel<br>Produkte vergleichen</div>
  <div class="abs social" aria-label="Soziale Netzwerke"><i></i><i></i><i></i><i></i><i></i></div>

  <div class="abs bottom-rule"></div>
  <div class="abs legal">Copyright © 2018 Waldhain Imkerei | Musterstraße 10 | 12345 Musterstadt | Tel. 012 345 678 | Fax 012 345 678 | info@waldhain-imkerei.de</div>
  <div class="abs pay" style="left:594px"></div>
  <div class="abs pay" style="left:644px"></div>
  <div class="abs pay" style="left:694px"></div>
  <div class="abs pay" style="left:744px"></div>
  <div class="abs pay" style="left:794px"></div>

</div>
</div>
</body>
</html>
```